Premium modern eliquids labels 84.5 x 80 mm

I am looking for modern graphics for the labels of a new eliquid line that will have 4 different types of eliquids. It will have a tobacco one (brown colours maybe), a fruity one (bright colours maybe), a minty one (green colours maybe) and a creamy one (beige colours maybe).
I will need one of them to see how the design is, that design will have to be adapted to the other 3 colours of the label.
The brand logo is attached. I also attached a sample of what is mandatory to write on the label, you can change size, place and font of what is written, the only thing that cannot be reduced is the yellow parts. I attach the bottle that we will use.The size of the label is 84.5 x 80 mm (base x height).

Target Market(s)

vapers

Requirements
Must have
• My project must have one of the labels.

```html
<!DOCTYPE html>
<html lang="it">
<head>
<meta charset="utf-8">
<title>Cleardrop Aromi – Mint label</title>
<link rel="stylesheet" href="https://fonts.googleapis.com/css2?family=Roboto+Condensed:wght@400;700;800&display=swap">
<style>
  :root {
    --page: #f4f6f7;
    --label-top: #5fb6d3;
    --label-mid: #3f9fc2;
    --label-deep: #2f86a8;
    --ink-white: #ffffff;
    --ink-dark: #10303d;
    --rule: rgba(16, 48, 61, 0.55);
    --badge: #f1b534;
    --panel-box: #eef1f2;
  }
  * { margin: 0; padding: 0; box-sizing: border-box; }
  html, body {
    width: 900px; height: 1200px; overflow: hidden;
    background: var(--page);
    font-family: "Roboto Condensed", "Arial Narrow", sans-serif;
  }
  .label {
    position: absolute; left: 40px; top: 210px;
    width: 820px; height: 776px;
    overflow: hidden; border-radius: 6px;
  }
  .label-surface {
    position: absolute; inset: 0;
    background:
      radial-gradient(circle at 30% 25%, rgba(255,255,255,0.18), transparent 55%),
      linear-gradient(160deg, var(--label-top), var(--label-mid) 55%, var(--label-deep));
  }
  .brand {
    position: absolute; color: var(--ink-white);
    font-weight: 800; text-align: center; line-height: 1;
  }
  .brand-name { display: block; letter-spacing: 1px; }
  .brand-sub { display: block; font-weight: 800; letter-spacing: 6px; }
  .brand--top { left: 24px; top: 128px; width: 300px; }
  .brand--top .brand-name { font-size: 50px; }
  .brand--top .brand-sub { font-size: 20px; margin-top: 6px; }
  .brand--bottom { left: 440px; top: 680px; width: 270px; }
  .brand--bottom .brand-name { font-size: 44px; }
  .brand--bottom .brand-sub { font-size: 18px; margin-top: 5px; }
  .flavour-name {
    position: absolute; left: 110px; top: 430px;
    transform: translate(-50%, -50%) rotate(-90deg);
    color: var(--ink-white);
    font-size: 112px; font-weight: 700; letter-spacing: 14px;
  }
  .volume {
    position: absolute; left: 54px; top: 710px;
    color: var(--ink-white); font-size: 34px; font-weight: 700;
  }
  .info-panel {
    position: absolute; left: 230px; top: 236px;
    width: 600px; height: 290px;
    transform: rotate(-90deg);
    color: var(--ink-dark);
    display: grid;
    grid-template-rows: 128px 34px 128px;
  }
  .info-row { display: grid; border-left: 1.5px solid var(--rule); }
  .info-row--usage { grid-template-columns: 330px 1fr; border-top: 1.5px solid var(--rule); }
  .info-row--lot { border-top: 1.5px solid var(--rule); border-bottom: 1.5px solid var(--rule);
    font-size: 16px; display: flex; align-items: center; padding-left: 60px; }
  .info-row--maker { grid-template-columns: 330px 1fr; border-left: none; }
  .info-cell { padding: 8px 10px; font-size: 17px; line-height: 1.15; }
  .info-cell + .info-cell { border-left: 1.5px solid var(--rule); }
  .info-cell strong { font-weight: 700; }
  .maker-box { border: 1.5px solid var(--rule); margin: 8px 0 0; padding: 8px 10px; font-size: 16px; line-height: 1.15; }
  .disposal { display: flex; gap: 28px; align-items: flex-start; padding: 10px 0 0 34px; }
  .disposal-item { display: flex; flex-direction: column; align-items: flex-start; gap: 2px; }
  .badge {
    background: var(--badge); color: var(--ink-dark);
    font-weight: 800; font-size: 15px; line-height: 0.95; padding: 3px 6px; text-transform: uppercase;
  }
  .disposal-part { font-size: 13px; font-weight: 700; text-transform: uppercase; }
</style>
</head>
<body>
  <section class="label">
    <div class="label-surface" role="img" aria-label="Blue background covered with water droplets"></div>

    <div class="brand brand--top">
      <span class="brand-name">CLEARDROP</span>
      <span class="brand-sub">AROMI</span>
    </div>

    <h1 class="flavour-name">MINT</h1>
    <p class="volume">20ml NET</p>

    <div class="brand brand--bottom">
      <span class="brand-name">CLEARDROP</span>
      <span class="brand-sub">AROMI</span>
    </div>

    <div class="info-panel">
      <div class="info-row info-row--usage">
        <p class="info-cell"><strong>ISTRUZIONI D'USO</strong>: Agitare bene prima dell'utilizzo. Diluire nelle percentuali consigliate sul nostro sito. Conservare in luogo fresco e asciutto</p>
        <p class="info-cell"><strong>INGREDIENTI</strong>: GLICOLE, PROPILENICO, SOSTANZE, AROMATIZZANTI</p>
      </div>
      <p class="info-row info-row--lot">L.SH20 - 001-PES-D.PROD.22-04-2022 D.SC.21-04-2024</p>
      <div class="info-row info-row--maker">
        <div class="maker-box">
          <strong>PRODOTTO E CONFEZIONATO</strong><br>
          DA Lumo Aromi srl Via dei Tigli 18<br>
          20100 Milano P.I.01234560789<br>
          Tel. +39 02 5550199<br>
          info@lumoaromi.it
        </div>
        <div class="disposal">
          <div class="disposal-item">
            <span class="badge">Raccolta<br>plastica</span>
            <span class="disposal-part">Etichetta</span>
            <span class="badge">PAP 5</span>
          </div>
          <div class="disposal-item">
            <span class="badge">Raccolta<br>plastica</span>
            <span class="disposal-part">Flacone</span>
            <span class="badge">PET 1</span>
          </div>
        </div>
      </div>
    </div>
  </section>
</body>
</html>
```